Law firm Seeks Modern and Engaging Site Redesign

Law firm seeks a new web site. Should be modern, but retaining existing logo. Needs to include contact section, professional bio, services offered, and contact information.

The site should be modern, responsive, and able to be SEO optimized.

The finished product should be coded in a Wordpress site, which I will provide. I can work with other platforms, including Wix, but WP is preferred.

Note the current site is https://www.tallowfieldlaw.example/#/home

Target Market(s)

Family Law Practice

Industry/Entity Type

Legal

Coding

Coded - Design and coding required

Number of Pages Required

4 page

Font styles to use
Sans Serif

Requirements
Must have
• Service description
Bio pages for partners
Contact Form
Awards/Publication page

```html
<!DOCTYPE html>
<html lang="en">
<head>
<meta charset="utf-8">
<title>Tallowfield Marsh — Attorneys at Law</title>
<link rel="stylesheet" href="https://fonts.googleapis.com/css2?family=Open+Sans:ital,wght@0,400;0,600;0,700;1,400&family=Roboto:wght@400;500&display=swap">
<style>
:root{
  --blue:#3a5bd9;
  --navy:#2f3f8f;
  --ink:#111;
  --body:#333;
  --grey:#666;
}
*{box-sizing:border-box;margin:0;padding:0}
html,body{width:1200px;height:3585px;overflow:hidden;background:#fff}
body{position:relative;font-family:'Roboto',Arial,sans-serif;color:var(--body)}
.abs{position:absolute}
.heading{font-family:'Open Sans',Arial,sans-serif;font-weight:700;color:var(--ink);font-size:42px;line-height:1}
.heading .bar{display:inline-block;width:4px;height:48px;background:var(--blue);margin-left:22px;vertical-align:-8px}
.btn{display:flex;align-items:center;justify-content:center;background:var(--blue);color:#fff;border-radius:30px;font-family:'Roboto',Arial,sans-serif;font-weight:500;font-size:15px;letter-spacing:.3px}

/* hero */
.hero{left:0;top:0;width:1200px;height:663px;background:linear-gradient(100deg,#9a9996 0%,#e6e5e1 30%,#cfcdc8 55%,#efeeea 75%,#a8a6a1 100%)}
.hero-glow{left:230px;top:180px;width:646px;height:260px;background:rgba(255,255,255,.35)}
.nav{left:0;top:0;width:1200px;height:67px;background:rgba(255,255,255,.55)}
.brand{left:88px;top:18px;font-family:'Open Sans',Arial,sans-serif;font-weight:400;font-size:24px;color:var(--grey);white-space:nowrap}
.menu a{position:absolute;top:24px;font-family:'Roboto',Arial,sans-serif;font-weight:500;font-size:14px;color:#222;text-decoration:none}
.menu a.active{color:var(--blue)}
.menu .phone{color:var(--blue);font-size:17px;top:21px;white-space:nowrap}
.hero-title{left:0;width:1200px;top:230px;text-align:center;font-family:'Open Sans',Arial,sans-serif;font-weight:700;font-size:72px;color:#111;white-space:nowrap}
.hero-tag{left:0;width:1200px;top:322px;text-align:center;font-family:'Open Sans',Arial,sans-serif;font-size:24px;letter-spacing:3px;color:var(--navy)}
.hero-btn{left:499px;top:378px;width:202px;height:54px;background:var(--navy);font-size:17px}
.scroll{left:576px;top:576px;width:46px;height:46px;border:1.5px solid #555;border-radius:50%}

/* about */
.about-photo{left:89px;top:764px;width:487px;height:382px;background:linear-gradient(90deg,#8f9399 0%,#c9cdd2 40%,#b7bbc0 70%,#5a4a3e 100%)}
.about-title{left:638px;top:782px}
.about-text{left:640px;top:840px;width:474px;font-size:14.5px;line-height:30.5px;text-align:justify}
.about-btn{left:640px;top:1079px;width:156px;height:43px}

/* services */
.svc-left{left:0;top:1243px;width:596px;height:586px;background:linear-gradient(135deg,#2b2626,#3f3335 60%,#1d1a1b)}
.svc-right{left:596px;top:1243px;width:604px;height:586px;background:linear-gradient(135deg,#3457d4,#2b45b0 60%,#3a5bd9)}
.svc-title{left:0;width:1200px;top:1335px;text-align:center;color:#fff;padding-left:30px}
.svc-col{color:#fff}
.svc-col h3{font-family:'Open Sans',Arial,sans-serif;font-weight:700;font-size:23px;margin-bottom:12px}
.svc-col p{font-size:14px;margin-bottom:13px}
.svc-col li{list-style:none;font-size:14px;line-height:27px;display:flex;align-items:center}
.svc-col li svg{margin-right:10px;flex:none}

/* bio */
.bio-title{left:0;width:1200px;top:1929px;text-align:center;padding-left:30px}
.card{width:237px;height:330px}
.card .ring{position:absolute;left:0;top:86px;width:237px;height:237px;border:2px solid var(--blue);border-radius:50%;background:#fff}
.card .photo{position:absolute;left:0;top:0;width:237px;height:237px;border-radius:50%;background:radial-gradient(circle at 50% 40%,#c9a892 0%,#7b6a62 35%,#3e3a40 70%,#2a2b33 100%)}
.card .name{position:absolute;left:0;width:237px;top:247px;text-align:center;font-family:'Open Sans',Arial,sans-serif;font-size:21px;line-height:23px;color:#111;white-space:nowrap}
.card .role{position:absolute;left:0;width:237px;top:275px;text-align:center;font-family:'Open Sans',Arial,sans-serif;font-style:italic;font-size:12.5px;color:#333}

/* contact form */
.talk{left:0;top:2415px;width:1200px;height:553px;background:linear-gradient(180deg,#2a1c17,#3a2720 50%,#241915)}
.talk-title{left:0;width:1200px;top:2513px;text-align:center;color:#fff;padding-left:20px}
.field{background:#fff;border:1px solid #ddd;font-size:16px;color:#666;padding:13px 18px;font-family:'Open Sans',Arial,sans-serif}
.submit{left:530px;top:2830px;width:140px;height:42px}

/* map + contact */
.map{left:0;top:2968px;width:607px;height:529px;background:linear-gradient(160deg,#eceae6,#e4e6e3 50%,#dfe9f0)}
.contact{left:607px;top:2968px;width:593px;height:529px;background:var(--blue);color:#fff}
.contact-title{left:665px;top:3068px;color:#fff}
.item{left:665px;color:#fff}
.item .ic{position:absolute;left:0;top:0;width:53px;height:53px;border:1.5px solid #fff;border-radius:50%;display:flex;align-items:center;justify-content:center}
.item h4{position:absolute;left:68px;top:0;font-family:'Roboto',Arial,sans-serif;font-weight:500;font-size:18px;white-space:nowrap}
.item p{position:absolute;left:68px;top:28px;font-size:14px;line-height:25px;white-space:nowrap}

/* footer */
.share{top:3522px}
.copy{left:0;width:1200px;top:3556px;text-align:center;font-size:12.5px;color:#333}
</style>
</head>
<body>

<!-- hero -->
<div class="abs hero" role="img" aria-label="Photo of white marble courthouse columns above stone steps"></div>
<div class="abs hero-glow"></div>
<header class="abs nav">
  <div class="abs brand">Tallowfield Marsh</div>
  <nav class="menu">
    <a class="active" style="left:344px">HOME</a>
    <a style="left:428px">ABOUT US</a>
    <a style="left:544px">SERVICES</a>
    <a style="left:657px">BIO</a>
    <a style="left:724px">AWARDS</a>
    <a style="left:829px">CONTACT US</a>
    <a class="phone" style="left:960px"><svg width="14" height="14" viewBox="0 0 24 24" style="vertical-align:-1px;margin-right:4px"><path fill="#3a5bd9" d="M6.6 10.8a15 15 0 0 0 6.6 6.6l2.2-2.2c.3-.3.7-.4 1-.2 1.1.4 2.3.6 3.6.6.6 0 1 .4 1 1V20c0 .6-.4 1-1 1A17 17 0 0 1 3 4c0-.6.4-1 1-1h3.5c.6 0 1 .4 1 1 0 1.3.2 2.5.6 3.6.1.3 0 .7-.2 1z"/></svg>(555) 014-2290</a>
  </nav>
</header>
<h1 class="abs hero-title">Tallowfield Marsh</h1>
<div class="abs hero-tag">Attorneys at Law</div>
<div class="abs btn hero-btn">GET STARTED</div>
<div class="abs scroll"><svg width="44" height="44" viewBox="0 0 44 44"><path d="M17 20l5 5 5-5" fill="none" stroke="#444" stroke-width="1.5"/></svg></div>

<!-- about -->
<div class="abs about-photo" role="img" aria-label="Photo of the two partners standing in the office lobby"></div>
<h2 class="abs heading about-title">Who We Are<span class="bar"></span></h2>
<p class="abs about-text">The law firm of Tallowfield Marsh, LLC is based in Bergen County, conveniently located in Ridgeford, New Jersey in 48 Millbrook Plaza. We serve the needs of clients throughout Bergen County, as well as, clients from several other counties, including, but not limited to, Passaic, Morris, Essex and Hudson. Between our partners, we have over 30+ years of experience assisting clients with all of their family law and criminal law needs.</p>
<div class="abs btn about-btn">READ MORE</div>

<!-- services -->
<div class="abs svc-left" role="img" aria-label="Dark photo of a client consulting with a lawyer"></div>
<div class="abs svc-right" role="img" aria-label="Blue-tinted photo of a person in handcuffs"></div>
<h2 class="abs heading svc-title" style="color:#fff">Services<span class="bar"></span></h2>
<div class="abs svc-col" style="left:90px;top:1408px">
  <h3>Family Law</h3>
  <p>Our firm accepts all kinds of family law matters, including:</p>
  <ul>
    <li><svg width="10" height="10" viewBox="0 0 10 10"><path d="M1 1l4 4-4 4M5 1l4 4-4 4" fill="none" stroke="#fff" stroke-width="1.3"/></svg>Divorce</li>
    <li><svg width="10" height="10" viewBox="0 0 10 10"><path d="M1 1l4 4-4 4M5 1l4 4-4 4" fill="none" stroke="#fff" stroke-width="1.3"/></svg>Child Custody</li>
    <li><svg width="10" height="10" viewBox="0 0 10 10"><path d="M1 1l4 4-4 4M5 1l4 4-4 4" fill="none" stroke="#fff" stroke-width="1.3"/></svg>Child Support</li>
    <li><svg width="10" height="10" viewBox="0 0 10 10"><path d="M1 1l4 4-4 4M5 1l4 4-4 4" fill="none" stroke="#fff" stroke-width="1.3"/></svg>Alimony</li>
    <li><svg width="10" height="10" viewBox="0 0 10 10"><path d="M1 1l4 4-4 4M5 1l4 4-4 4" fill="none" stroke="#fff" stroke-width="1.3"/></svg>Division of Assets and Liabilities</li>
    <li><svg width="10" height="10" viewBox="0 0 10 10"><path d="M1 1l4 4-4 4M5 1l4 4-4 4" fill="none" stroke="#fff" stroke-width="1.3"/></svg>Pre-nuptial agreements</li>
    <li><svg width="10" height="10" viewBox="0 0 10 10"><path d="M1 1l4 4-4 4M5 1l4 4-4 4" fill="none" stroke="#fff" stroke-width="1.3"/></svg>High-net worth and complex divorce cases</li>
    <li><svg width="10" height="10" viewBox="0 0 10 10"><path d="M1 1l4 4-4 4M5 1l4 4-4 4" fill="none" stroke="#fff" stroke-width="1.3"/></svg>Domestic violence</li>
    <li><svg width="10" height="10" viewBox="0 0 10 10"><path d="M1 1l4 4-4 4M5 1l4 4-4 4" fill="none" stroke="#fff" stroke-width="1.3"/></svg>DCP&amp;P (formerly DYFS)</li>
    <li><svg width="10" height="10" viewBox="0 0 10 10"><path d="M1 1l4 4-4 4M5 1l4 4-4 4" fill="none" stroke="#fff" stroke-width="1.3"/></svg>Support Modification</li>
  </ul>
</div>
<div class="abs svc-col" style="left:707px;top:1408px">
  <h3>Criminal Law</h3>
  <p>Our firm accepts all kinds of criminal law matters, including:</p>
  <ul>
    <li><svg width="10" height="10" viewBox="0 0 10 10"><path d="M1 1l4 4-4 4M5 1l4 4-4 4" fill="none" stroke="#fff" stroke-width="1.3"/></svg>Assault</li>
    <li><svg width="10" height="10" viewBox="0 0 10 10"><path d="M1 1l4 4-4 4M5 1l4 4-4 4" fill="none" stroke="#fff" stroke-width="1.3"/></svg>Domestic Violence</li>
    <li><svg width="10" height="10" viewBox="0 0 10 10"><path d="M1 1l4 4-4 4M5 1l4 4-4 4" fill="none" stroke="#fff" stroke-width="1.3"/></svg>Drug Crimes</li>
    <li><svg width="10" height="10" viewBox="0 0 10 10"><path d="M1 1l4 4-4 4M5 1l4 4-4 4" fill="none" stroke="#fff" stroke-width="1.3"/></svg>DWI/DUI</li>
    <li><svg width="10" height="10" viewBox="0 0 10 10"><path d="M1 1l4 4-4 4M5 1l4 4-4 4" fill="none" stroke="#fff" stroke-width="1.3"/></svg>Sex Crimes</li>
    <li><svg width="10" height="10" viewBox="0 0 10 10"><path d="M1 1l4 4-4 4M5 1l4 4-4 4" fill="none" stroke="#fff" stroke-width="1.3"/></svg>Theft/Fraud Crimes</li>
    <li><svg width="10" height="10" viewBox="0 0 10 10"><path d="M1 1l4 4-4 4M5 1l4 4-4 4" fill="none" stroke="#fff" stroke-width="1.3"/></svg>Expungements</li>
  </ul>
</div>

<!-- bio -->
<h2 class="abs heading bio-title">Bio<span class="bar"></span></h2>
<div class="abs card" style="left:90px;top:1995px">
  <div class="ring"></div>
  <div class="photo" role="img" aria-label="Portrait of partner Daniel R. Tallowfield"></div>
  <div class="name">Daniel R. Tallowfield</div>
  <div class="role">Area of family law</div>
</div>
<div class="abs card" style="left:351px;top:1995px">
  <div class="ring"></div>
  <div class="photo" role="img" aria-label="Portrait of partner Owen P. Marsh"></div>
  <div class="name">Owen P. Marsh</div>
  <div class="role">Area of family law</div>
</div>
<div class="abs card" style="left:612px;top:1995px">
  <div class="ring"></div>
  <div class="photo" role="img" aria-label="Portrait of attorney Lena M. Hartwell" style="background:radial-gradient(circle at 50% 40%,#d8b39c 0%,#8a6a58 35%,#c9c9c9 75%,#e3e3e3 100%)"></div>
  <div class="name">Lena M. Hartwell</div>
  <div class="role">family and divorce law,</div>
</div>
<div class="abs card" style="left:873px;top:1995px">
  <div class="ring"></div>
  <div class="photo" role="img" aria-label="Portrait of attorney Sofia A. Renaldi" style="background:radial-gradient(circle at 50% 40%,#c99a82 0%,#8a6b5c 35%,#3a3636 75%,#222 100%)"></div>
  <div class="name" style="top:237px">Sofia A.<br>Renaldi</div>
  <div class="role" style="top:289px">Area of family law</div>
</div>

<!-- contact form -->
<div class="abs talk" role="img" aria-label="Dark photo of law books on library shelves"></div>
<h2 class="abs heading talk-title" style="color:#fff">Let’s Talk<span class="bar"></span></h2>
<div class="abs field" style="left:141px;top:2586px;width:452px;height:48px">Name</div>
<div class="abs field" style="left:607px;top:2586px;width:452px;height:48px">Email</div>
<div class="abs field" style="left:141px;top:2649px;width:452px;height:48px">Phone No</div>
<div class="abs field" style="left:607px;top:2649px;width:452px;height:48px">Practise Area</div>
<div class="abs field" style="left:141px;top:2712px;width:918px;height:101px">Message</div>
<div class="abs btn submit">SUBMIT</div>

<!-- map + contact -->
<div class="abs map" role="img" aria-label="Street map showing the office location with a red pin"></div>
<div class="abs contact"></div>
<h2 class="abs heading contact-title" style="color:#fff">Contact Us<span class="bar" style="background:#fff"></span></h2>
<div class="abs item" style="top:3132px">
  <div class="ic"><svg width="22" height="20" viewBox="0 0 24 22"><path d="M12 2L1 11h3v9h6v-6h4v6h6v-9h3z" fill="#fff"/></svg></div>
  <h4>Address</h4>
  <p>Tallowfield &amp; Marsh LLC,48 Millbrook Plaza<br>Drive Suite 210,Ridgeford, NJ 07000</p>
</div>
<div class="abs item" style="top:3236px">
  <div class="ic"><svg width="16" height="16" viewBox="0 0 24 24"><path fill="#fff" d="M6.6 10.8a15 15 0 0 0 6.6 6.6l2.2-2.2c.3-.3.7-.4 1-.2 1.1.4 2.3.6 3.6.6.6 0 1 .4 1 1V20c0 .6-.4 1-1 1A17 17 0 0 1 3 4c0-.6.4-1 1-1h3.5c.6 0 1 .4 1 1 0 1.3.2 2.5.6 3.6.1.3 0 .7-.2 1z"/></svg></div>
  <h4>Phone No</h4>
  <p>(555) 014-2290</p>
</div>
<div class="abs item" style="top:3317px">
  <div class="ic"><svg width="20" height="20" viewBox="0 0 24 24"><rect x="6" y="2" width="12" height="7" fill="none" stroke="#fff" stroke-width="2"/><rect x="3" y="9" width="18" height="12" rx="1" fill="#fff"/><rect x="8" y="13" width="8" height="2" fill="#3a5bd9"/></svg></div>
  <h4>Fax</h4>
  <p>(555) 014-2291</p>
</div>

<!-- footer -->
<footer>
  <svg class="abs share" style="left:577px" width="16" height="16" viewBox="0 0 24 24" aria-label="Share"><circle cx="18" cy="5" r="3" fill="#222"/><circle cx="6" cy="12" r="3" fill="#222"/><circle cx="18" cy="19" r="3" fill="#222"/><path d="M8.6 10.7l6.8-4M8.6 13.3l6.8 4" stroke="#222" stroke-width="2"/></svg>
  <svg class="abs share" style="left:604px" width="16" height="16" viewBox="0 0 24 24" aria-label="Email"><rect x="2" y="5" width="20" height="14" rx="2" fill="none" stroke="#222" stroke-width="2"/><path d="M3 6l9 7 9-7" fill="none" stroke="#222" stroke-width="2"/></svg>
  <p class="abs copy">© Copyright 2020 The Company name. All Rights Reserved.</p>
</footer>

</body>
</html>
```